Web Site Redesign

We operate a data centre facility specialing in colocation and Fibre optic connectivity (i.e. point to point fibre services and internet over fibre).

We have an existing site located at www.norvalex.example however this is very very tired and requires a redesign. We are looking for a fresh new design that will be appealing to potential customers.

The Company name is Norva eX and the primary corporate colour is bright red with secondary colours of white, grey and black. Specific bright red can be seen in attached company logo.

Website needs to be modern, clean and professional representing our premium colocation and fibre provider branding.

Our company slogan is : safe. secure. reliable

We will provide feedback regardless of the quality of the design to ensure a better outcome for all parties.

Please feel free to contact us if you have any questions.

# The designer can use placeholder images or feel free to use any/all or none of the attached images
# The designer can use sample filler text

Target Market(s)

Technical IT Professionals as well C level executives (i.e. CEO's, CIO).

Industry/Entity Type

Internet

Requirements
Must have
• clean design
Nice to have
• A sidebar with two sections. 1 for current promo and 1 for "Let us call you back/contact you"
Should not have
• Clutter

```html
<!DOCTYPE html>
<html lang="en">
<head>
<meta charset="utf-8">
<title>Norva eX — Safe. Secure. Reliable.</title>
<link rel="stylesheet" href="https://fonts.googleapis.com/css2?family=Open+Sans:wght@400;600;700&display=swap">
<style>
  :root {
    --red: #d9272a;
    --red-dark: #b01518;
    --red-light: #e23a3c;
    --ink: #333333;
    --ink-dark: #222222;
    --grey-field: #e6e6e6;
    --grey-frame: #e1e1e1;
    --grey-footer: #e8e8e8;
    --white: #ffffff;
  }
  * { margin: 0; padding: 0; box-sizing: border-box; }
  html, body { width: 1200px; height: 1057px; overflow: hidden; background: var(--white); }
  body { position: relative; font-family: "Open Sans", Arial, sans-serif; color: var(--ink); }

  .brand {
    position: absolute; left: 57px; top: 13px; width: 137px; height: 138px;
    display: flex; flex-direction: column; align-items: flex-start; justify-content: flex-end;
    padding: 0 0 8px 18px; gap: 12px;
  }
  .brand-mark { width: 40px; height: 40px; background: var(--red); }
  .brand-name {
    font-size: 20px; font-weight: 600; color: var(--ink-dark);
    text-transform: uppercase; letter-spacing: 1px; white-space: nowrap;
  }

  .main-nav {
    position: absolute; left: 211px; top: 116px; width: 907px; height: 35px;
    background: linear-gradient(var(--red-light), var(--red-dark));
    border-radius: 5px; display: flex; align-items: center; padding-left: 16px;
  }
  .main-nav a {
    color: var(--white); text-decoration: none; font-size: 15px; font-weight: 600;
    padding: 0 16px; line-height: 22px; border-left: 1px solid rgba(0,0,0,0.25);
  }
  .main-nav a:first-child { border-left: none; padding-left: 10px; }

  .hero {
    position: absolute; left: 76px; top: 161px; width: 1042px; height: 271px;
    border: 3px solid var(--grey-frame); border-radius: 4px;
    background: linear-gradient(90deg, #3a3a3e 0%, #55555a 30%, #2b2b2e 45%, #6e2a2e 62%, #a23036 72%, #8c8a86 85%, #d8d4cc 100%);
  }
  .hero-banner {
    position: absolute; left: 76px; top: 322px; width: 575px; height: 94px;
    background: var(--red); color: var(--white); padding: 12px 0 0 31px;
  }
  .hero-banner h1 { font-size: 45px; font-weight: 600; line-height: 52px; letter-spacing: -0.5px; text-shadow: 1px 1px 2px rgba(0,0,0,0.3); }
  .hero-banner p { font-size: 16px; font-weight: 600; line-height: 20px; }

  .intro { position: absolute; left: 75px; top: 448px; width: 690px; }
  .intro h2 { color: var(--red); font-size: 18px; font-weight: 600; margin-bottom: 19px; }
  .intro p { font-size: 13.5px; font-weight: 600; line-height: 18.5px; margin-bottom: 18px; }

  .promo {
    position: absolute; left: 784px; top: 453px; width: 334px; height: 228px;
    border-radius: 3px; overflow: hidden;
    background: linear-gradient(90deg, #5a3a1a 0%, #c8b02a 25%, #d8c63a 45%, #6a2024 65%, #222 100%);
  }
  .promo-caption {
    position: absolute; left: 0; right: 0; bottom: 0; height: 90px;
    background: rgba(0,0,0,0.6); color: var(--white); padding: 10px 10px 10px 12px;
  }
  .promo-caption h3 { font-size: 16px; font-weight: 600; margin-bottom: 4px; }
  .promo-caption p { font-size: 11.5px; font-weight: 700; line-height: 13.5px; }
  .promo-caption a { color: var(--red-light); text-decoration: none; margin-left: 4px; }

  .callback-title { position: absolute; left: 784px; top: 693px; width: 335px; height: 56px; }
  .callback-title span {
    position: absolute; left: 0; top: 6px; width: 334px; text-align: center;
    color: var(--white); font-size: 17.5px; font-weight: 600;
  }

  .callback-form { position: absolute; left: 784px; top: 753px; width: 334px; }
  .field { display: flex; align-items: flex-start; height: 26px; }
  .field label { width: 96px; font-size: 13.5px; font-weight: 600; color: var(--ink); line-height: 16px; }
  .field .input { width: 237px; height: 22px; background: var(--grey-field); }
  .field.comments { height: 96px; }
  .field.comments .input { height: 82px; }
  .submit {
    position: absolute; left: 96px; top: 198px; width: 237px; height: 31px;
    background: linear-gradient(var(--red-light), var(--red-dark)); border: 2px solid var(--grey-frame);
    border-radius: 4px; color: var(--white); font-family: inherit; font-size: 14px; font-weight: 700;
  }

  .site-footer {
    position: absolute; left: 76px; top: 1018px; width: 1042px; height: 39px;
    background: var(--grey-footer); border-radius: 4px 4px 0 0;
    display: flex; align-items: center; justify-content: space-between; padding: 0 18px 0 16px;
    font-size: 12px; font-weight: 600; color: var(--ink);
  }
  .footer-links a { color: var(--ink); text-decoration: none; }
  .footer-links .sep { margin: 0 8px; }
</style>
</head>
<body>
  <div class="brand">
    <span class="brand-mark"></span>
    <span class="brand-name">Norva eX</span>
  </div>

  <nav class="main-nav">
    <a href="#">Home</a><a href="#">About Us</a><a href="#">Facilities</a><a href="#">Business Continuity</a><a href="#">Services</a><a href="#">Partners</a><a href="#">Webmail</a><a href="#">Contact Us</a>
  </nav>

  <div class="hero" role="img" aria-label="Photo of server racks inside the data centre"></div>
  <div class="hero-banner">
    <h1>Safe. Secure. Reliable.</h1>
    <p>Norva eX's Safe, Secure &amp; Reliable Data Centre</p>
  </div>

  <section class="intro">
    <h2>A world class data centre in the safest place on Earth.</h2>
    <p>With a centrally located data centre in the heart of the Perth CBD Norva eX is excellently positioned<br>to assist with your critical IT requirements.</p>
    <p>The CBD facility features overlapping power grids, redundant power supplies and comprehensively<br>maintained infrastructure,&nbsp; providing excellent levels of protection for your critical IT equipment.<br>The State's newest and most technologically advanced data centre is also now open in Belmont, a<br>convenient 5.5 km's from the CBD providing a perfect location for either production sites, or DR<br>infrastructure.</p>
    <p>From Government departments to large corporations to SME's, Norva eX is the ideal company to<br>assist with your colocation requirements. With warm racks already provisioned, you can begin<br>using the data centre almost immediately.</p>
    <p>Call us today to see how we can help meet your needs.</p>
  </section>

  <aside class="promo" role="img" aria-label="Photo of yellow and black equipment cabinets in a data hall">
    <div class="promo-caption">
      <h3>Current Promotion</h3>
      <p>Lorem ipsum dolor sit amet, consectetur adipiscing<br>elit. Ut pharetra gravida dui, ut semper odio euismod<br>in.<a href="#">Learn more &gt;&gt;</a></p>
    </div>
  </aside>

  <div class="callback-title">
    <svg width="335" height="56" viewBox="0 0 335 56">
      <path d="M5 0 H329 Q334 0 334 5 V37 Q334 42 329 42 H282 L265 56 L268 42 H5 Q0 42 0 37 V5 Q0 0 5 0 Z" fill="#d9272a"/>
    </svg>
    <span>&ldquo;Let us call you back / contact you&rdquo;</span>
  </div>

  <form class="callback-form">
    <div class="field"><label>Name:</label><span class="input"></span></div>
    <div class="field"><label>Company:</label><span class="input"></span></div>
    <div class="field"><label>Phone:</label><span class="input"></span></div>
    <div class="field"><label>Email:</label><span class="input"></span></div>
    <div class="field comments"><label>Comments:</label><span class="input"></span></div>
    <button class="submit" type="button">Submit</button>
  </form>

  <footer class="site-footer">
    <span>&copy; Norva eX 2010.</span>
    <span class="footer-links">
      <a href="#">Privacy</a><span class="sep">|</span><a href="#">Copyright</a><span class="sep">|</span><a href="#">Terms &amp; Conditions</a><span class="sep">|</span><a href="#">Site Map</a><span class="sep">|</span><a href="#">Contact Us</a>
    </span>
  </footer>
</body>
</html>
```